Responsive and Updated Website

I need a refresh of kelvornix.com. The next gen site needs to be responsive. Looking for updated header, navbar and footer as well as responsive design. Need new templates for

homepage,
product family page,
product page,
support page.

I started doing this myself at sandbox.kelvornix.com but no time to finish.

Two row navbar and two levels of submenu on navbar requried.

Color scheme to remain the same #005da9 and #78A22F are logo blue and green. Dreamweaver templates for deliverable

Must complete asap.

Target Market(s)

B2B

Coding

Coded - Design and coding required

Number of Pages Required

4 page

Font styles to use
Sans Serif

Requirements
Must have
• Bootstrap responsive design or similar.
• Header
• Navbar
• Footer
• Hero panel and other page content 9/12ths of homepage with sidebar as per sandbox.kelvornix.com

```html
<!DOCTYPE html>
<html lang="en">
<head>
<meta charset="utf-8">
<title>Kelvornix – Monitoring and Control</title>
<link rel="stylesheet" href="https://fonts.googleapis.com/css2?family=Roboto:wght@400;500;700&family=Teko:wght@500;600&family=Questrial&display=swap">
<style>
  :root {
    --brand-blue: #005da9;
    --brand-green: #78a22f;
    --topbar-bg: #283540;
    --topbar-text: #ffffff;
    --social-bg: #5c6670;
    --client-btn: #48535d;
    --nav-text: #3b4248;
    --heading-dark: #2b3640;
    --body-text: #1f2328;
    --hero-light: #f3f3f2;
    --hero-mid: #e6e9ec;
    --hero-blue: #b9d2ea;
  }
  * { box-sizing: border-box; margin: 0; padding: 0; }
  html, body { width: 1200px; height: 603px; overflow: hidden; }
  body { font-family: "Roboto", Arial, sans-serif; background: #fff; position: relative; }

  .topbar { position: absolute; left: 0; top: 0; width: 1200px; height: 40px; background: var(--topbar-bg); color: var(--topbar-text); }
  .social { position: absolute; left: 109px; top: 11px; display: flex; gap: 6px; }
  .social span { width: 18px; height: 18px; border-radius: 50%; background: var(--social-bg); display: block; }
  .topbar-item { position: absolute; top: 0; height: 40px; display: flex; align-items: center; gap: 5px; font-size: 11px; font-weight: 500; }
  .topbar-item.phone { left: 589px; font-size: 12.5px; font-weight: 700; gap: 7px; }
  .topbar-item.webmail { left: 726px; }
  .topbar-item.livechat { left: 807px; }
  .topbar-item.support { left: 888px; }
  .client-area { position: absolute; left: 973px; top: 8px; width: 87px; height: 25px; background: var(--client-btn); font-size: 11px; font-weight: 500; display: flex; align-items: center; justify-content: center; gap: 5px; }
  .cart { position: absolute; left: 1076px; top: 9px; }
  .cart-count { position: absolute; left: 1089px; top: 10px; width: 13px; height: 12px; background: var(--brand-green); font-size: 8px; font-weight: 700; text-align: center; line-height: 12px; }

  .navbar { position: absolute; left: 0; top: 40px; width: 1200px; height: 95px; background: #fff; border-bottom: 1px solid #dcdcdc; }
  .brand { position: absolute; left: 128px; top: 26px; font-family: "Roboto", Arial, sans-serif; font-weight: 700; font-size: 35px; letter-spacing: -1px; color: var(--brand-blue); }
  .menu { position: absolute; top: 0; height: 95px; left: 0; width: 100%; }
  .menu a { position: absolute; top: 41px; font-size: 12px; color: var(--nav-text); text-decoration: none; letter-spacing: 0.2px; }
  .search { position: absolute; left: 1080px; top: 41px; }

  .hero { position: absolute; left: 0; top: 136px; width: 1200px; height: 467px; overflow: hidden; }
  .hero-photo { position: absolute; inset: 0; background: linear-gradient(90deg, var(--hero-light) 0%, var(--hero-light) 55%, var(--hero-mid) 72%, var(--hero-blue) 85%, var(--hero-mid) 100%); }
  .hero-eyebrow { position: absolute; left: 127px; top: 105px; font-size: 24px; font-weight: 700; letter-spacing: 1px; color: var(--heading-dark); }
  .hero-title { position: absolute; left: 126px; top: 140px; font-family: "Teko", "Arial Narrow", sans-serif; font-weight: 600; font-size: 60px; line-height: 48px; color: var(--brand-blue); letter-spacing: 0.5px; }
  .hero-text { position: absolute; left: 127px; top: 243px; width: 520px; font-family: "Questrial", Arial, sans-serif; font-size: 14.5px; line-height: 17.5px; color: var(--body-text); }
  .hero-button { position: absolute; left: 130px; top: 331px; width: 130px; height: 46px; background: var(--topbar-bg); color: #fff; font-size: 11.5px; font-weight: 700; display: flex; align-items: center; justify-content: center; }
  .slider-dots { position: absolute; left: 577px; top: 442px; display: flex; align-items: center; gap: 5px; }
  .slider-dots span { width: 10px; height: 10px; border-radius: 50%; background: #1d1d1d; border: 3px solid #1d1d1d; box-shadow: inset 0 0 0 1px #fff; }
  .slider-dots span.active { width: 3px; height: 3px; border: none; box-shadow: none; margin-right: 4px; }
</style>
</head>
<body>
  <header class="topbar">
    <div class="social"><span></span><span></span><span></span><span></span><span></span></div>
    <div class="topbar-item phone">
      <svg width="17" height="17" viewBox="0 0 17 17"><circle cx="8.5" cy="8.5" r="8.5" fill="#5c6670"/><path d="M5.5 4.5l1.6-.4 1 2.2-1 .8a6 6 0 0 0 2.6 2.6l.8-1 2.2 1-.4 1.6c-3.5.3-7.1-3.3-6.8-6.8z" fill="#fff"/></svg>
      (800) 555-0147
    </div>
    <div class="topbar-item webmail">
      <svg width="13" height="10" viewBox="0 0 13 10"><path d="M0 3l6.5-3L13 3v7H0z" fill="#8b949c"/><path d="M0 3l6.5 4L13 3" stroke="#283540" fill="none"/></svg>
      WebMail
    </div>
    <div class="topbar-item livechat">
      <svg width="14" height="11" viewBox="0 0 14 11"><rect x="0" y="0" width="9" height="7" rx="2" fill="#8b949c"/><rect x="5" y="4" width="9" height="7" rx="2" fill="#8b949c" stroke="#283540"/></svg>
      LiveChat
    </div>
    <div class="topbar-item support">
      <svg width="12" height="12" viewBox="0 0 12 12"><circle cx="6" cy="6" r="6" fill="#8b949c"/><text x="6" y="9.5" text-anchor="middle" font-size="9" font-weight="700" fill="#283540" font-family="Arial">?</text></svg>
      Support
    </div>
    <div class="client-area">
      <svg width="9" height="10" viewBox="0 0 9 10"><circle cx="4.5" cy="2.5" r="2.5" fill="#aab2b9"/><path d="M0 10a4.5 4.5 0 0 1 9 0z" fill="#aab2b9"/></svg>
      Client Area
    </div>
    <svg class="cart" width="20" height="18" viewBox="0 0 20 18"><path d="M1 6h18l-2.5 10h-13z" fill="none" stroke="#8b949c" stroke-width="1.5"/><path d="M5 6l4-5M15 6l-4-5M6 9v4M10 9v4M14 9v4" stroke="#8b949c" stroke-width="1.2"/></svg>
    <div class="cart-count">0</div>
  </header>

  <nav class="navbar">
    <div class="brand">kelvornix</div>
    <div class="menu">
      <a style="left:473px">PRODUCTS</a>
      <a style="left:563px">PARTNERS</a>
      <a style="left:652px">SUPPORT</a>
      <a style="left:734px">NEWS</a>
      <a style="left:797px">ABOUT</a>
      <a style="left:866px">CAREERS</a>
      <a style="left:946px">CONTACT</a>
      <a style="left:1029px">SHOP</a>
    </div>
    <svg class="search" width="14" height="14" viewBox="0 0 14 14"><circle cx="5.8" cy="5.8" r="4.8" fill="none" stroke="#3b4248" stroke-width="1.4"/><path d="M9.3 9.3L13 13" stroke="#3b4248" stroke-width="1.6"/></svg>
  </nav>

  <section class="hero">
    <div class="hero-photo" role="img" aria-label="Smiling woman in a light blue denim shirt working on a laptop in a bright office with sticky notes on the wall"></div>
    <h2 class="hero-eyebrow">MONITORING AND CONTROL</h2>
    <h1 class="hero-title">I DON'T HAVE TIME TO GO ONSITE<br>EVERY TIME I NEED TO CLOSE A GATE.</h1>
    <p class="hero-text">Don't waste time operating non-networked devices. Bring command and control systems onto your network and start saving time and money with Kelvornix monitoring and control.</p>
    <div class="hero-button">LEARN MORE</div>
    <div class="slider-dots"><span class="active"></span><span></span><span></span><span></span></div>
  </section>
</body>
</html>
```